Online Psychiatry business - Business Card

I need a business card design. The target audience is busy professionals of any field (this therapy appeals best to 24-35 year olds). It involves psychiatry by tele-medicine (or video-conference). Nothing on it should be a giveaway that it's about mental health. Professional design with silver or gold as the primary colors appeals to me. The card must be as simple and as uncluttered as possible. Some color and flowing design on the edge of the card appeals to me.
CrestMindLink.com should probably appear in the center of the card and stand out, i.e. bold lettering, and easy to read, no cursive, but Ariel Black. Some where below this, should appear "Too Busy to Take Care of Yourself? Think again." Since this isn't office based, I don't think an office address is necessary and limits clutter.
Information that does need to appear is my name: Gerald Whitcombe, MD
General phone number: 541-876-2209. I'm hoping to get an 24-hour answering service soon so leave a little room for this. In addition I want to include two email addresses:
CrestMindLink@maildrop-box.com and CrestMind247@maildrop-box.com
Updates

I like the designs. I would like someone to put the website in bold in the center

 as most have been doing with a smaller font reminder nearby saying "No time" etc.
but I'd like to put my name down in the corner with the rest of the contact material.
Black print against a white or grey background appeals to me, with darker silver artwork near the sides (simple abstract, like wavy lines or something you can one up with that works. 
thanks

I ve tried to provide as much feedback as possible given my time limits, so if you have extra questions, please feel free to email. I tried to attach a file of a business card I really like but make be difficult to actually manufacture. I'm going to send you a link to the photo. The card has a pull tab. There is not much information on the outside. In fact, if you were to design the outside, I would just print : Too Busy to Take Care of Yourself? Think Again.

When you pull the tab the remaining information is on the bottom half of the card. Please don't use the color pink!!!!
http://www.layoutgallerypost.com/2009/05/100-clever-card-ideas/
It is the 39th photo on the list, about 2/3ds of the way down the page. It is titled: Faltenkästli

#7 and #16 have an appeal to me, except for the dot patterns
Hope this helps

I'm running out of time and energy. I 've been trying to give do down the list and give  individual feedback but I won't be able to do that anymore.

So if you have any specific questions, write me, and again thank you for all your effort!!

I know i received your files, including your zip files, Plonix,

but Gideon, did you send me the files including ZIP on project 5914386?
thanks

Target Market(s)

Working professionals and executive, attorneys, etc.

Industry/Entity Type

Business

Logo Text

Don't Have Time to Take Care of Yourself? Think Again.

Logo styles of interest
Pictorial/Combination Logo
Wordmark Logo
Other font styles liked:
• Ariel Black appeals to me the most

Requirements
Must have
• Want to emphasize that the website must be obvious, easily found (The CrestMindLink.com)
For that reason i'd like the card to be white, and minimal decoration on one or both sides just to add some style and color
Nice to have
• A Very uncluttered, elegant design, and something that makes it stick in your head-doesn't everyone want the last?
Should not have
• Nothing on the card that give it away that this is about psychiatry, such as brain or other symbol, but also nothing that gives it away as a medical business, such as a stethoscope or red cross or anything.

```html
<!DOCTYPE html>
<html lang="en">
<head>
<meta charset="utf-8">
<title>CrestMindLink.com – Business Card</title>
<link rel="stylesheet" href="https://fonts.googleapis.com/css2?family=Archivo+Black&family=Open+Sans:wght@400;600;700&display=swap">
<style>
  :root {
    --backdrop: #2e2520;
    --card-white: #ffffff;
    --ink: #2b2b2b;
    --ink-soft: #555555;
    --accent-orange: #e48f1c;
    --gold-deep: #a66d1e;
    --gold-mid: #d7b45a;
    --gold-light: #fbf3a4;
    --gold-pale: #fffbe0;
    --silver-dark: #6d6d6d;
    --silver-light: #e2e2e2;
    --white-text: #ffffff;
  }
  * { box-sizing: border-box; margin: 0; padding: 0; }
  html, body {
    width: 1200px; height: 418px; overflow: hidden;
    background: var(--backdrop);
  }
  .canvas {
    position: relative; width: 1200px; height: 418px;
  }
  .card {
    position: absolute; top: 90px;
    width: 464px; height: 266px;
    box-shadow: 0 6px 18px rgba(0,0,0,0.45);
    overflow: hidden;
  }
  /* Front */
  .card-front { left: 124px; background: var(--card-white); }
  .front-swoosh { position: absolute; inset: 0; width: 464px; height: 266px; }
  .doctor-name {
    position: absolute; left: 25px; top: 14px;
    font-family: "Open Sans", Arial, sans-serif;
    font-size: 18px; color: var(--white-text); letter-spacing: 0.2px;
  }
  .front-website {
    position: absolute; left: 0; right: 0; top: 128px;
    text-align: center;
    font-family: "Archivo Black", "Arial Black", sans-serif;
    font-size: 22px; color: var(--ink);
  }
  .front-tagline {
    position: absolute; right: 46px; top: 160px;
    font-family: "Open Sans", Arial, sans-serif;
    font-size: 11px; color: var(--accent-orange);
  }
  .contact-phone {
    position: absolute; left: 21px; top: 223px;
    font-family: "Open Sans", Arial, sans-serif;
  }
  .phone-line { font-size: 11px; color: var(--ink); }
  .phone-label { color: var(--accent-orange); }
  .answering-note { font-size: 9.5px; color: var(--accent-orange); margin-top: 4px; }
  .contact-email {
    position: absolute; left: 224px; top: 224px;
    display: flex; align-items: center; gap: 10px;
  }
  .email-icon { width: 26px; height: 26px; }
  .email-list {
    font-family: "Open Sans", Arial, sans-serif;
    font-size: 10.5px; color: var(--ink-soft); line-height: 15px;
  }
  /* Back */
  .card-back {
    left: 626px;
    background: linear-gradient(180deg, var(--gold-light) 0%, #eccf74 40%, #cfa048 75%, #b47f2c 100%);
    text-align: center;
  }
  .back-website {
    position: absolute; left: 0; right: 0; top: 129px;
    font-family: "Archivo Black", "Arial Black", sans-serif;
    font-size: 23px; color: var(--white-text);
    text-shadow: 0 1px 2px rgba(90,55,10,0.35);
  }
  .back-tagline {
    position: absolute; left: 0; right: 0; top: 165px;
    font-family: "Open Sans", Arial, sans-serif;
    font-weight: 700; font-size: 10.5px; color: #111; letter-spacing: 0.3px;
  }
</style>
</head>
<body>
<main class="canvas">
  <section class="card card-front" aria-label="Card front">
    <svg class="front-swoosh" viewBox="0 0 464 266" aria-hidden="true">
      <defs>
        <linearGradient id="goldSweep" x1="0" y1="0" x2="1" y2="0">
          <stop offset="0" stop-color="var(--gold-deep)"/>
          <stop offset="0.45" stop-color="var(--gold-mid)"/>
          <stop offset="0.8" stop-color="var(--gold-light)"/>
          <stop offset="1" stop-color="var(--gold-pale)"/>
        </linearGradient>
        <linearGradient id="silverSweep" x1="0" y1="0" x2="1" y2="0">
          <stop offset="0" stop-color="var(--silver-light)"/>
          <stop offset="0.6" stop-color="var(--silver-dark)"/>
          <stop offset="1" stop-color="#9a9a9a"/>
        </linearGradient>
      </defs>
      <path d="M0 0 H464 V2 C330 18 140 50 0 128 Z" fill="url(#goldSweep)"/>
      <path d="M30 110 C150 50 320 16 464 2 V24 C320 30 160 60 30 110 Z" fill="url(#silverSweep)"/>
    </svg>
    <p class="doctor-name">Gerald Whitcombe, MD</p>
    <h1 class="front-website">CrestMindLink.com</h1>
    <p class="front-tagline">Too Busy to Take Care of Yourself? Think again.</p>
    <div class="contact-phone">
      <p class="phone-line"><span class="phone-label">General Phone:</span> 541-876-2209</p>
      <p class="answering-note">24-hour answering service</p>
    </div>
    <div class="contact-email">
      <svg class="email-icon" viewBox="0 0 26 26" aria-hidden="true">
        <rect x="1" y="5" width="24" height="17" rx="2" fill="#c89a3e" stroke="#8a6220"/>
        <path d="M1 6 L13 15 L25 6" fill="none" stroke="#fff6cf" stroke-width="1.5"/>
        <circle cx="13" cy="11" r="3" fill="none" stroke="#3a2a10" stroke-width="1.2"/>
      </svg>
      <div class="email-list">
        <p>CrestMindLink@maildrop-box.com</p>
        <p>CrestMind247@maildrop-box.com</p>
      </div>
    </div>
  </section>

  <section class="card card-back" aria-label="Card back">
    <h2 class="back-website">CrestMindLink.com</h2>
    <p class="back-tagline">NO TIME TO TAKE CARE OF YOURSELF?</p>
  </section>
</main>
</body>
</html>
```